Printed Fitted Table Cloth

Looking to place my business name and logo on a table cloth for promotions and other marketing activities.

Our business name is:
Bright Summit Rugby League Academy

Mission statement: "Mentoring Rugby League's Next Generation"

Target Market(s)

U/14s - U/18s

Colors
ffffff
cadf82
add136
9bcb3b
eaf2ce
f6faec

Requirements
Must have
• Would like to keep greens and whites in project.
Should not have
• And Navy colour

```html
<!DOCTYPE html>
<html lang="en">
<head>
<meta charset="utf-8">
<title>Bright Summit Rugby League Academy – Table Cloth</title>
<link rel="stylesheet" href="https://fonts.googleapis.com/css2?family=Bebas+Neue&family=Montserrat:wght@600&display=swap">
<style>
  :root {
    --white: #ffffff;
    --lime-bright: #cadf3a;
    --lime: #add136;
    --green: #9bcb3b;
    --shadow-green: rgba(60, 130, 30, 0.55);
  }
  html, body {
    margin: 0;
    padding: 0;
    overflow: hidden;
  }
  .tablecloth {
    position: relative;
    width: 1200px;
    height: 415px;
    overflow: hidden;
  }
  .tablecloth__backdrop {
    position: absolute;
    inset: 0;
    background:
      radial-gradient(ellipse 60% 70% at 50% 45%, var(--green) 0%, transparent 70%),
      linear-gradient(100deg, var(--lime-bright) 0%, var(--lime) 25%, var(--green) 55%, var(--lime) 85%, var(--lime-bright) 100%);
  }
  .brand-lockup {
    position: absolute;
    left: 500px;
    top: 100px;
    display: flex;
    align-items: center;
    gap: 30px;
  }
  .brand-lockup__symbol {
    display: block;
    width: 72px;
    height: 72px;
  }
  .brand-lockup__name {
    margin: 0;
    font-family: "Montserrat", sans-serif;
    font-weight: 600;
    font-size: 42px;
    letter-spacing: 1px;
    line-height: 1;
    color: var(--white);
    padding-top: 22px;
  }
  .academy-name {
    position: absolute;
    left: 0;
    right: 0;
    top: 220px;
    margin: 0;
    text-align: center;
    font-family: "Bebas Neue", sans-serif;
    font-weight: 400;
    font-size: 45px;
    letter-spacing: 1.3px;
    line-height: 1;
    color: var(--white);
    text-shadow: 3px 4px 4px var(--shadow-green);
  }
</style>
</head>
<body>
  <main class="tablecloth">
    <div class="tablecloth__backdrop" role="img" aria-label="Lime to green gradient background with a soft halftone dot texture"></div>
    <div class="brand-lockup">
      <svg class="brand-lockup__symbol" viewBox="0 0 72 72" role="img" aria-label="Academy logo mark">
        <circle cx="36" cy="36" r="33" fill="none" stroke="var(--white)" stroke-width="5"/>
      </svg>
      <p class="brand-lockup__name">BSRLA</p>
    </div>
    <h1 class="academy-name">Bright Summit Rugby League Academy</h1>
  </main>
</body>
</html>
```